Structural Engineering Firm Looking for High-Impact Lead Generation Focused Design (for B2B)

A well-established structural engineering firm in the UK wants a new website designed for them which will help them realise more business from online. Directly through the website as well as Ads and lead platforms. They need to compare favourably to competitors and have clarity. Current Site is here: http://www.marlowgrantpartners.example/ - you can take imagery from this site if you want to help with the design.
Updates

Target Market(s)

Homeowners, Architects, Designers, Construction Companies and Landlords

Industry/Entity Type

Professional Services

Number of Pages Required

5+ page

Font styles to use
Sans Serif

Requirements
Must have
• A Strong, Simple and Professional Design with a Focus on Lead Generation
Nice to have
• Creativity in the Detail, Clear Messaging
Should not have
• Too Much Colour, Too 'Consumer', Too Much Variation

```html
<!DOCTYPE html>
<html lang="en">
<head>
<meta charset="utf-8">
<title>Marlow Grant Partners – Structural Engineering &amp; Party Wall Surveying</title>
<link href="https://fonts.googleapis.com/css2?family=Gentium+Book+Plus:wght@400;700&family=Lato:wght@400;700&display=swap" rel="stylesheet">
<style>
:root{
  --purple:#3d2e44;
  --purple-dark:#2f2336;
  --red:#c1272d;
  --accent:#df4b35;
  --ink:#2b2b2b;
  --body:#4a4a4a;
  --grey:#efefef;
  --black:#111;
  --white:#fff;
}
*{box-sizing:border-box;margin:0;padding:0}
html,body{width:1200px;height:4766px;overflow:hidden}
body{position:relative;background:var(--white);font-family:"Lato",sans-serif;color:var(--body)}
.abs{position:absolute}
.serif{font-family:"Gentium Book Plus",serif}
h2.section-title{font-family:"Gentium Book Plus",serif;font-weight:400;font-size:32px;line-height:42px;color:var(--ink)}
h2.section-title b{font-weight:700}
p.copy{font-size:17px;line-height:30px;text-align:justify}
.btn{position:absolute;display:flex;align-items:center;justify-content:center;gap:12px;background:var(--accent);color:var(--white);font-size:17px;border-radius:4px;height:50px}
.btn svg{width:9px;height:14px}
.select{position:absolute;background:var(--white);border:2px solid var(--purple);border-radius:6px;display:flex;align-items:center;justify-content:space-between;padding:0 24px;font-size:17px;color:var(--ink)}
.caret{width:0;height:0;border-left:6px solid transparent;border-right:6px solid transparent;border-top:7px solid var(--red)}

/* header */
.topnav{top:16px;right:110px;display:flex;gap:40px;font-size:15px;color:var(--ink)}
.mainbar{top:59px;left:0;width:1200px;height:41px}
.mainnav{top:59px;right:110px;height:41px;display:flex;align-items:center;gap:42px;font-size:15px;color:var(--white)}
.brand{top:20px;left:111px;font-family:"Gentium Book Plus",serif;font-size:34px;line-height:30px;color:#1a1a1a;letter-spacing:-.5px}

/* hero */
.hero-media{top:100px;left:0;width:1200px;height:580px;background:linear-gradient(180deg,#5f7a52 0%,#8a9a7e 35%,#b7b4a6 55%,#6d7a58 80%,#4c5f3a 100%)}
.hero-title{top:212px;left:0;width:1200px;text-align:center;font-family:"Gentium Book Plus",serif;font-weight:700;font-size:40px;line-height:55px;color:var(--white)}
.hero-sub{top:446px;left:0;width:1200px;text-align:center;font-size:21px;font-weight:700;color:var(--white)}
.arrow{top:336px;width:20px;height:40px}

/* photo placeholders */
.photo{position:absolute}
.frame{position:absolute}

/* stages */
.stages{top:1605px;left:0;width:1200px;height:562px;background:linear-gradient(120deg,var(--purple-dark),var(--purple) 50%,var(--purple-dark))}
.stage{position:absolute;top:1818px;width:230px;height:268px;border:2px solid #e8e8e8}
.stage span{position:absolute;left:26px;bottom:26px;color:var(--white);font-weight:700;font-size:17px}

/* partnership */
.partner{top:2701px;left:0;width:1200px;height:553px;background:var(--purple)}
.partner-media{top:2701px;left:0;width:760px;height:553px;background:linear-gradient(90deg,#8a5a44 0%,#9b6a50 35%,#a07c63 55%,rgba(61,46,68,1) 100%)}
.partner p{color:var(--white)}

/* news */
.news-card{position:absolute;top:3406px;width:240px;height:342px;background:var(--white);box-shadow:0 2px 10px rgba(0,0,0,.15)}
.news-card .pic{height:203px}
.news-date{position:absolute;top:227px;left:20px;display:flex;align-items:center;gap:12px;color:var(--accent);font-size:19px}
.news-text{position:absolute;top:263px;left:20px;right:12px;font-size:17px;line-height:29px;color:var(--ink)}

/* offices */
.offices{top:3851px;left:0;width:1200px;height:480px;background:var(--grey)}
.office{position:absolute;top:3916px;width:470px;height:287px;background:var(--white);box-shadow:0 3px 10px rgba(0,0,0,.18)}
.office-shadow{position:absolute;top:3928px;width:470px;height:287px;background:var(--purple);transform:rotate(.8deg)}
.office .map{position:absolute;left:0;top:0;width:210px;height:100%}
.office .info{position:absolute;left:236px;top:32px;font-size:15px;line-height:30px;color:var(--ink)}
.office h3{font-family:"Gentium Book Plus",serif;font-size:21px;line-height:29px;font-weight:700;color:#1a1a1a;margin-bottom:14px}
.row{display:flex;align-items:center;gap:8px}
.ico{width:11px;height:14px}

/* footer */
.footer{top:4327px;left:0;width:1200px;height:439px;background:var(--black);color:var(--white)}
.foot-brand{top:4370px;left:111px;font-family:"Gentium Book Plus",serif;font-size:30px;line-height:26px;color:var(--white)}
.foot-nav{top:4386px;right:110px;display:flex;gap:30px;font-size:17px;color:var(--white)}
.foot-col{position:absolute;top:4462px;font-size:15px;line-height:30px;color:var(--white)}
.foot-col strong{font-weight:700;font-size:16px}
.foot-rule{top:4706px;left:111px;width:980px;height:1px;background:#333}
.copyright{top:4727px;left:0;width:1200px;text-align:center;font-size:15px;color:var(--white)}
</style>
</head>
<body>

<!-- header -->
<svg class="abs mainbar" viewBox="0 0 1200 41" preserveAspectRatio="none"><polygon points="370,0 1200,0 1200,41 385,41" fill="var(--purple)"/></svg>
<svg class="abs" style="top:0;left:330px" width="60" height="100" viewBox="0 0 60 100"><polygon points="0,0 20,0 55,100 0,100" fill="#fff"/></svg>
<div class="abs brand">MARLOW GRANT<br>PARTNERS</div>
<nav class="abs topnav"><span>Gallery</span><span>Blog</span><span>About Us</span><span>Cotact Us</span></nav>
<nav class="abs mainnav"><span>Structural Design</span><span>Structural Surveys</span><span>Planning</span><span>Party Wall</span><span>Partners</span></nav>

<!-- hero -->
<div class="abs hero-media" role="img" aria-label="Modern two-storey house with large glazing set in a wooded garden"></div>
<svg class="abs" style="top:600px;left:0" width="1200" height="80" viewBox="0 0 1200 80"><polygon points="0,28 600,56 1200,28 1200,80 0,80" fill="var(--red)"/><polygon points="0,46 600,76 1200,46 1200,80 0,80" fill="#fff"/></svg>
<h1 class="abs hero-title">Efficient &amp; Professional Structural<br>Engineering &amp; Party Wall<br>Surveying</h1>
<div class="abs hero-sub">Get a Competitive Quote from the local experts</div>
<div class="select" style="top:498px;left:408px;width:384px;height:58px;border:none">What services are you looking for?<span class="caret"></span></div>
<svg class="abs arrow" style="left:46px" viewBox="0 0 20 40"><polyline points="16,4 4,20 16,36" fill="none" stroke="#fff" stroke-width="2"/></svg>
<svg class="abs arrow" style="left:1134px" viewBox="0 0 20 40"><polyline points="4,4 16,20 4,36" fill="none" stroke="#fff" stroke-width="2"/></svg>

<!-- structural engineers -->
<h2 class="abs section-title" style="top:786px;left:111px"><b>Structural Engineers</b> in London<br>&amp; the South East</h2>
<p class="abs copy" style="top:892px;left:111px;width:550px">Sed ut perspiciatis unde omnis iste natus error sit voluptatem accusantium doloremque laudantium, totam rem aperiam, eaque ipsa quae ab illo inventore veritatis et quasi architecto beatae vitae dicta sunt explicabo. Nemo enim ipsam voluptatem quia voluptas sit aspernatur aut odit aut fugit, sed quia consequuntur magni dolores eos qui ratione voluptatem sequi nesciunt.</p>
<svg class="abs" style="top:780px;left:718px" width="380" height="360" viewBox="0 0 380 360"><polygon points="14,8 374,8 370,340 4,352" fill="none" stroke="var(--red)" stroke-width="3"/></svg>
<div class="photo" role="img" aria-label="Tall brick townhouse lit at dusk with stone entrance steps" style="top:693px;left:734px;width:357px;height:428px;background:linear-gradient(160deg,#5a6f8f 0%,#6b5c52 40%,#8d7c6c 70%,#c9c3b6 100%);clip-path:polygon(0 16%,55% 16%,60% 0,64% 16%,100% 16%,100% 100%,0 100%)"></div>

<!-- party wall -->
<svg class="abs" style="top:1160px;left:100px" width="400" height="380" viewBox="0 0 400 380"><polygon points="0,14 384,14 372,370 0,370" fill="var(--accent)"/></svg>
<div class="photo" role="img" aria-label="Contemporary rear extension on a brick semi-detached home" style="top:1119px;left:111px;width:362px;height:410px;background:linear-gradient(170deg,#8a95a6 0%,#a99b8c 35%,#ece8e1 55%,#5f5a55 80%,#6d7a4c 100%);clip-path:polygon(0 17%,28% 17%,28% 0,62% 0,62% 17%,100% 17%,100% 100%,0 100%)"></div>
<h2 class="abs section-title" style="top:1232px;left:536px">Choose the <b>party wall specialista</b></h2>
<p class="abs copy" style="top:1295px;left:539px;width:552px">Sed ut perspiciatis unde omnis iste natus error sit voluptatem accusantium doloremque laudantium, totam rem aperiam, eaque ipsa quae ab illo inventore veritatis et quasi architecto beatae vitae dicta sunt explicabo. Nemo enim ipsam voluptatem quia voluptas sit aspernatur aut odit aut fugit, sed quia consequuntur magni dolores eos qui ratione voluptatem sequi nesciunt.</p>

<!-- stages -->
<div class="abs stages"></div>
<h2 class="abs section-title" style="top:1660px;left:111px;color:#fff"><b>From drawing to delivered</b><br>We support you every step of the way</h2>
<div class="btn" style="top:1697px;left:919px;width:170px">Find Out More <svg viewBox="0 0 9 14"><polyline points="2,2 7,7 2,12" fill="none" stroke="#fff" stroke-width="2"/></svg></div>
<div class="stage" style="left:111px" role="img" aria-label="Bright kitchen with steel-framed glazing"><div style="position:absolute;inset:0;background:linear-gradient(180deg,#e8e6e2,#a9a7a3 60%,#3a3838)"></div><span>Brief</span></div>
<div class="stage" style="left:360px" role="img" aria-label="Open-plan living room with grey sofa"><div style="position:absolute;inset:0;background:linear-gradient(180deg,#d9d7d3,#8c8a86 60%,#3d3c3a)"></div><span>Design</span></div>
<div class="stage" style="left:610px" role="img" aria-label="Industrial-style dining space with copper pendants"><div style="position:absolute;inset:0;background:linear-gradient(180deg,#f0eeea,#9c8c7a 55%,#3a2f28)"></div><span>Refine</span></div>
<div class="stage" style="left:861px" role="img" aria-label="Period terrace houses under a blue sky"><div style="position:absolute;inset:0;background:linear-gradient(180deg,#3f6fb8,#6a8fc4 40%,#4a3a33 75%,#2a2422)"></div><span>Deliver</span></div>

<!-- fast turnaround -->
<h2 class="abs section-title" style="top:2233px;left:111px">Need a <b>fast turnaround?</b></h2>
<p class="abs copy" style="top:2290px;left:111px;width:550px">Sed ut perspiciatis unde omnis iste natus error sit voluptatem accusantium doloremque laudantium, totam rem aperiam, eaque ipsa quae ab illo inventore veritatis et quasi architecto beatae vitae dicta sunt explicabo.</p>
<div class="select" style="top:2426px;left:111px;width:388px;height:61px">What services are you looking for?<span class="caret"></span></div>
<p class="abs copy" style="top:2510px;left:111px;width:550px">Sed ut perspiciatis unde omnis iste natus error sit voluptatem accusantium doloremque laudantium.</p>
<div class="btn" style="top:2587px;left:111px;width:189px">Book a Site Visit <svg viewBox="0 0 9 14"><polyline points="2,2 7,7 2,12" fill="none" stroke="#fff" stroke-width="2"/></svg></div>
<svg class="abs" style="top:2244px;left:684px" width="410" height="390" viewBox="0 0 410 390"><polygon points="6,10 403,24 403,386 22,386" fill="var(--red)"/></svg>
<div class="photo" role="img" aria-label="Brick extension with a timber fence and glazed door" style="top:2262px;left:700px;width:387px;height:364px;background:linear-gradient(100deg,#b86a4a 0%,#a45638 40%,#d7d3cc 60%,#4f4f52 100%)"></div>

<!-- partnership -->
<div class="abs partner"></div>
<div class="abs partner-media" role="img" aria-label="Red-brick house with arched French doors and a stone terrace"></div>
<h2 class="abs section-title" style="top:2780px;left:615px;color:#fff">We work in <b>Partnership</b></h2>
<div class="abs" style="top:2845px;left:615px;width:480px;font-size:17px;line-height:30px;color:#fff">Sed ut perspiciatis unde omnis iste natus error sit volupt accusantium doloremque laudantium.</div>
<div class="abs" style="top:2914px;left:615px;font-size:17px;color:#fff">If you would like to explore partnering with Marlow Grant:</div>
<div class="btn" style="top:2966px;left:615px;width:188px">Partner with us <svg viewBox="0 0 9 14"><polyline points="2,2 7,7 2,12" fill="none" stroke="#fff" stroke-width="2"/></svg></div>
<div class="abs" style="top:3043px;left:615px;width:480px;font-size:17px;line-height:30px;color:#fff">If you have a project with existing architects &amp; builders, but want to introduce then:</div>
<div class="btn" style="top:3123px;left:615px;width:276px">Introduce us to your team <svg viewBox="0 0 9 14"><polyline points="2,2 7,7 2,12" fill="none" stroke="#fff" stroke-width="2"/></svg></div>

<!-- news -->
<h2 class="abs section-title" style="top:3314px;left:0;width:1200px;text-align:center"><b>News, Events &amp; Features</b></h2>
<div class="news-card" style="left:104px"><div class="pic" role="img" aria-label="Construction workers in hard hats reviewing a tablet" style="background:linear-gradient(180deg,#c9ccd0,#7f8a9a 50%,#6b5a4c)"></div><div class="news-date"><svg width="18" height="18" viewBox="0 0 18 18"><rect x="1" y="3" width="16" height="14" rx="2" fill="var(--accent)"/><rect x="4" y="0" width="2" height="5" fill="var(--accent)"/><rect x="12" y="0" width="2" height="5" fill="var(--accent)"/><rect x="1" y="6" width="16" height="1.5" fill="#fff"/></svg>20-5-2022</div><div class="news-text">Nemo enim ipsam volu ptatem quia voluptas</div></div>
<div class="news-card" style="left:355px"><div class="pic" role="img" aria-label="Dining room with exposed brick wall" style="background:linear-gradient(180deg,#a0664a,#8a5a42 50%,#5a4032)"></div><div class="news-date"><svg width="18" height="18" viewBox="0 0 18 18"><rect x="1" y="3" width="16" height="14" rx="2" fill="var(--accent)"/><rect x="4" y="0" width="2" height="5" fill="var(--accent)"/><rect x="12" y="0" width="2" height="5" fill="var(--accent)"/><rect x="1" y="6" width="16" height="1.5" fill="#fff"/></svg>20-5-2022</div><div class="news-text">Nemo enim ipsam volu ptatem quia voluptas</div></div>
<div class="news-card" style="left:605px"><div class="pic" role="img" aria-label="Business team discussing plans at a desk" style="background:linear-gradient(180deg,#e4e2de,#9a9590 55%,#3d3a38)"></div><div class="news-date"><svg width="18" height="18" viewBox="0 0 18 18"><rect x="1" y="3" width="16" height="14" rx="2" fill="var(--accent)"/><rect x="4" y="0" width="2" height="5" fill="var(--accent)"/><rect x="12" y="0" width="2" height="5" fill="var(--accent)"/><rect x="1" y="6" width="16" height="1.5" fill="#fff"/></svg>20-5-2022</div><div class="news-text">Nemo enim ipsam volu ptatem quia voluptas</div></div>
<div class="news-card" style="left:856px"><div class="pic" role="img" aria-label="Dark-clad rear extension with sliding glass doors" style="background:linear-gradient(180deg,#b7b2ab,#4a4644 50%,#8b8d6e)"></div><div class="news-date"><svg width="18" height="18" viewBox="0 0 18 18"><rect x="1" y="3" width="16" height="14" rx="2" fill="var(--accent)"/><rect x="4" y="0" width="2" height="5" fill="var(--accent)"/><rect x="12" y="0" width="2" height="5" fill="var(--accent)"/><rect x="1" y="6" width="16" height="1.5" fill="#fff"/></svg>20-5-2022</div><div class="news-text">Nemo enim ipsam volu ptatem quia voluptas</div></div>

<!-- offices -->
<div class="abs offices"></div>
<div class="office-shadow" style="left:117px"></div>
<div class="office" style="left:111px">
  <div class="map" role="img" aria-label="Street map of the London office area" style="background:linear-gradient(135deg,#eceae4,#dcdad2 60%,#cfd6cf)"></div>
  <div class="info">
    <h3>Marlow Grant Partners<br>London</h3>
    <div class="row"><svg class="ico" viewBox="0 0 11 14"><path d="M5.5 0A5 5 0 0 0 .5 5c0 4 5 9 5 9s5-5 5-9a5 5 0 0 0-5-5z" fill="var(--red)"/><circle cx="5.5" cy="5" r="2" fill="#fff"/></svg>Main Office:</div>
    Unit 4 Hallam Works<br>27 Cresswell Lane<br>London SE9 4QP
    <div class="row" style="margin-top:10px"><svg class="ico" viewBox="0 0 14 14"><path d="M3 1l2 3-1.5 1.5a8 8 0 0 0 5 5L10 9l3 2-1 2.5C6 13 1 8 .5 2z" fill="var(--red)"/></svg>+44(0) 20 7946 0318</div>
  </div>
</div>
<div class="office-shadow" style="left:627px"></div>
<div class="office" style="left:621px">
  <div class="map" role="img" aria-label="Regional map of the Sussex coast office area" style="background:linear-gradient(180deg,#9ccf9a,#86bf86 60%,#6fa3d8 75%,#6fa3d8)"></div>
  <div class="info">
    <h3>Marlow Grant Partners<br>Sussex</h3>
    <div class="row"><svg class="ico" viewBox="0 0 11 14"><path d="M5.5 0A5 5 0 0 0 .5 5c0 4 5 9 5 9s5-5 5-9a5 5 0 0 0-5-5z" fill="var(--red)"/><circle cx="5.5" cy="5" r="2" fill="#fff"/></svg>Main Office:</div>
    Street<br>County<br>Postcode
    <div class="row" style="margin-top:10px"><svg class="ico" viewBox="0 0 14 14"><path d="M3 1l2 3-1.5 1.5a8 8 0 0 0 5 5L10 9l3 2-1 2.5C6 13 1 8 .5 2z" fill="var(--red)"/></svg>+44(0) 1632 960 244</div>
  </div>
</div>

<!-- footer -->
<svg class="abs" style="top:4280px;left:0" width="1200" height="60" viewBox="0 0 1200 60"><polygon points="0,30 600,2 1200,30 1200,60 0,60" fill="var(--red)"/><polygon points="0,42 600,10 1200,42 1200,60 0,60" fill="var(--black)"/></svg>
<div class="abs footer" style="top:4340px;height:426px"></div>
<div class="abs foot-brand">MARLOW GRANT<br>PARTNERS</div>
<nav class="abs foot-nav"><span>Partners</span><span>Gallery</span><span>Blog</span><span>About Us</span><span>Contact Us</span></nav>
<div class="foot-col" style="left:111px"><strong>Design</strong><br>Design advice<br>Lofts<br>Side returns<br>Basements<br>House conversion<br>Temporary works</div>
<div class="foot-col" style="left:335px"><strong>Planning</strong><br>planning applications<br>Planning Reports<br><br><strong>Survey</strong></div>
<div class="foot-col" style="left:583px"><strong>Party Wall</strong><br>Serving party wall notices<br>Forming party wall awards<br>Condition schedules<br>Minor residential works &amp; schemes</div>
<div class="foot-col" style="left:917px"><strong>Contact Marlow Grant</strong><br>Send an Email<br><strong>London</strong><br><span class="row"><svg class="ico" viewBox="0 0 14 14"><path d="M3 1l2 3-1.5 1.5a8 8 0 0 0 5 5L10 9l3 2-1 2.5C6 13 1 8 .5 2z" fill="var(--red)"/></svg>+44(0) 20 7946 0318</span><strong>Sussex</strong><br><span class="row"><svg class="ico" viewBox="0 0 14 14"><path d="M3 1l2 3-1.5 1.5a8 8 0 0 0 5 5L10 9l3 2-1 2.5C6 13 1 8 .5 2z" fill="var(--red)"/></svg>+44(0) 1632 960 244</span></div>
<div class="abs foot-rule"></div>
<div class="abs copyright">2022 Marlow Grant Partners. All Rights Reserved.</div>

</body>
</html>
```